The First Annual Tamsworth Legacy Supper

Something similar to the attached but an attention grabber. It needs to attract people with money to spend!

```html
<!DOCTYPE html>
<html lang="en">
<head>
<meta charset="utf-8">
<title>The First Annual Tamsworth Legacy Supper</title>
<link rel="stylesheet" href="https://fonts.googleapis.com/css2?family=Montserrat:wght@500;600;700;800;900&family=Playfair+Display:ital,wght@0,700;0,900;1,900&family=Figtree:wght@400;600;700;800&display=swap">
<style>
  :root {
    --navy: #283583;
    --white: #ffffff;
    --red: #d62a2a;
    --black: #0a0a0a;
    --ink: #1d1d1f;
    --backdrop: #8b8b8b;
  }
  html, body {
    margin: 0;
    width: 1200px;
    height: 1200px;
    overflow: hidden;
    background: var(--backdrop);
  }
  .flyer {
    position: absolute;
    left: 152px;
    top: 20px;
    width: 926px;
    height: 1200px;
    background: var(--white);
    transform: scale(0.9667);
    transform-origin: top left;
    overflow: hidden;
    font-family: "Figtree", sans-serif;
    color: var(--navy);
  }
  .top-band {
    position: absolute; left: 0; top: 0; width: 926px; height: 252px;
    background: var(--navy);
  }
  .presenter {
    position: absolute; left: 173px; top: 55px; width: 580px; height: 33px;
    background: var(--white);
    display: flex; align-items: center; justify-content: center;
    white-space: nowrap;
    font-family: "Montserrat", sans-serif; font-weight: 800;
    font-size: 15px; letter-spacing: 2.6px; color: var(--navy);
  }
  .title-art { position: absolute; left: 0; top: 0; width: 926px; height: 430px; }
  .date-row {
    position: absolute; left: 0; top: 428px; width: 926px; height: 62px;
    display: flex; align-items: center; justify-content: center; gap: 18px;
    font-family: "Montserrat", sans-serif; color: var(--navy);
  }
  .date-row .month, .date-row .year { font-size: 42px; font-weight: 600; letter-spacing: 8px; }
  .date-row .day { font-size: 76px; font-weight: 800; line-height: 1; }
  .date-row .divider { width: 2px; height: 58px; background: var(--red); }
  .rule-red { position: absolute; left: 211px; width: 504px; height: 2px; background: var(--red); }
  .time-block {
    position: absolute; left: 0; top: 505px; width: 926px; text-align: center;
    font-family: "Montserrat", sans-serif; color: var(--navy);
  }
  .time-block .lead { font-size: 22px; font-weight: 600; letter-spacing: 6px; line-height: 26px; }
  .time-block .time { font-size: 64px; font-weight: 800; line-height: 62px; letter-spacing: 2px; }
  .time-block .tail { font-size: 22px; font-weight: 600; letter-spacing: 6px; line-height: 26px; }
  .edge-bar { position: absolute; background: var(--black); }
  .features {
    position: absolute; left: 55px; top: 639px; width: 390px;
  }
  .features h2 {
    margin: 0 0 6px; font-family: "Montserrat", sans-serif; font-weight: 800;
    font-size: 24px; line-height: 23px; letter-spacing: 1.2px; color: var(--navy);
  }
  .features p {
    margin: 0 0 9px; font-size: 16px; line-height: 21px; color: var(--ink); font-weight: 400;
  }
  .venue-photo {
    position: absolute; left: 473px; top: 639px; width: 399px; height: 259px;
    background: linear-gradient(180deg, #5f9bd6 0%, #a9c9e8 42%, #e8eef2 58%, #8aa05c 78%, #6f8a44 100%);
  }
  .social {
    position: absolute; left: 473px; top: 911px; width: 399px;
    border-top: 2px solid var(--navy); padding-top: 14px;
    display: flex; gap: 12px; align-items: flex-start;
  }
  .social .mark { width: 30px; height: 30px; border-radius: 6px; background: var(--navy); flex: none; margin-top: 2px; }
  .social p { margin: 0; font-size: 14.5px; line-height: 20px; font-weight: 700; color: var(--navy); }
  .bottom-band {
    position: absolute; left: 0; top: 970px; width: 926px; height: 230px;
    background: var(--navy); color: var(--white);
  }
  .ticket-prices {
    position: absolute; left: 55px; top: 22px; width: 310px;
    font-weight: 700; font-size: 16px; line-height: 23px; text-transform: uppercase;
  }
  .ticket-prices p { margin: 0 0 22px; }
  .outlets { position: absolute; top: 22px; font-size: 16px; line-height: 21px; }
  .outlets h3 {
    margin: 0 0 6px; display: inline-block; font-size: 17px; font-weight: 800;
    padding-bottom: 3px; border-bottom: 2px solid var(--white);
  }
  .outlets p { margin: 0; }
  .outlets strong { font-weight: 700; display: block; }
  .outlets.stores { left: 408px; }
  .outlets.contacts { left: 721px; }
</style>
</head>
<body>
  <main class="flyer">
    <div class="top-band"></div>
    <div class="presenter">THE TAMSWORTH COMMUNITY CENTER PRESENTS</div>

    <svg class="title-art" viewBox="0 0 926 430" aria-label="The First Annual Tamsworth Legacy Supper">
      <g font-family="Playfair Display, serif" fill="#ffffff">
        <line x1="349" y1="121" x2="392" y2="121" stroke="#ffffff" stroke-width="1.5"/>
        <line x1="349" y1="150" x2="392" y2="150" stroke="#ffffff" stroke-width="1.5"/>
        <text x="370" y="146" font-size="25" font-weight="700" text-anchor="middle">The</text>
        <text x="443" y="163" font-size="66" font-weight="700" text-anchor="middle">1st</text>
        <line x1="494" y1="121" x2="578" y2="121" stroke="#ffffff" stroke-width="1.5"/>
        <line x1="494" y1="150" x2="578" y2="150" stroke="#ffffff" stroke-width="1.5"/>
        <text x="536" y="146" font-size="25" font-weight="700" text-anchor="middle">Annual</text>
      </g>
      <text x="133" y="252" font-family="Montserrat, sans-serif" font-weight="900" font-size="108"
            fill="#ffffff" textLength="660" lengthAdjust="spacingAndGlyphs">TAMSWORTH</text>
      <text x="163" y="336" font-family="Montserrat, sans-serif" font-weight="900" font-size="116"
            fill="#283583" textLength="600" lengthAdjust="spacingAndGlyphs">LEGACY</text>
      <text x="463" y="402" font-family="Playfair Display, serif" font-style="italic" font-weight="900"
            font-size="88" fill="#0a0a0a" text-anchor="middle" transform="rotate(-3 463 380)">Supper</text>
    </svg>

    <div class="date-row">
      <span class="month">APRIL</span>
      <span class="divider"></span>
      <span class="day">23</span>
      <span class="divider"></span>
      <span class="year">2022</span>
    </div>
    <div class="rule-red" style="top:498px"></div>

    <div class="time-block">
      <div class="lead">STARTING AT</div>
      <div class="time">5:00PM</div>
      <div class="tail">WITH COCKTAIL HOUR</div>
    </div>
    <div class="rule-red" style="top:617px"></div>

    <div class="edge-bar" style="left:0;top:642px;width:28px;height:61px"></div>
    <div class="edge-bar" style="left:902px;top:639px;width:24px;height:259px"></div>

    <section class="features">
      <h2>LIVE AUCTION, SILENT<br>AUCTION, RAFFLE<br>AND A CASH BAR!</h2>
      <p>Come on out to the Tamsworth Community Center for a delicious prime rib dinner, drinks, entertainment and more! There will be plenty of amazing auction items for everyone to choose from.</p>
      <p>All proceeds will go to the Tamsworth Community Center. We will share some history of the school and each year we will highlight a local family. This year will be the Hollis family who have been here for ....years!!</p>
      <p>High Side Barn, dirt bike, custom knives, a pack trip and so much more!</p>
    </section>

    <div class="venue-photo" role="img" aria-label="Photo of the white community center building under a blue sky with a grassy lawn"></div>

    <div class="social">
      <span class="mark"></span>
      <p>Follow the Tamsworth Community Center's Commons page to see all the auction items available!</p>
    </div>

    <footer class="bottom-band">
      <div class="ticket-prices">
        <p>Tickets for the event are $50 each or $90 for a couple</p>
        <p>Tickets for the 10x12 High Side Barn $25 each or 5 for $100. Donated by: Northfork Shed Center of Eldridge, value $6500</p>
      </div>
      <div class="outlets stores">
        <h3>Get your tickets from:</h3>
        <p><strong>Northfork Shed Center in Eldridge</strong>42 Quarry Rd, Eldridge</p>
        <p><strong>Silver Ridge Real Estate</strong>210 W Aspen St, Eldridge</p>
        <p><strong>Tamsworth Store</strong>4410 County Road 12, Tamsworth</p>
      </div>
      <div class="outlets contacts">
        <h3>Or get them from</h3>
        <p><strong>Dana Morrow -</strong>(555)014-2287</p>
        <p><strong>Lynn Carver -</strong>(555)019-4631</p>
      </div>
    </footer>
  </main>
</body>
</html>
```